Eye catching Bottle label for pink gin targeting women 25+

We need a new label for a re-launch of our shimmering strawberry pink gin liqueur. We would like it to look premium and eye catching on the shelf. We have 2 labels we require, one for 200ml bottle (2x2 inches) and one for 500ml bottle 4x4 inches). Label must state the ml of the bottle abd that it is 18.75%Vol. Also say Shimmering Strawberry Gin Liqueur with the brand name at the top - Harlow Vale Distillers. We have a logo but it doesn't need to be used if it doesn't work with the design/colours. The gin is presented in a clear bottle and is pink and sparkly. See uploaded image for reference.

Target Market(s)

Women aged 25-45

Font styles to use
Decorative

Colors
f59296
fbd4d5
eea4c8

Requirements
Must have
• Bottle size - 500ml/200ml
• Must say 18.75% Vol
• Must have brand name - Harlow Vale Distillers
• Must have product name - Shimmering Pink Strawberry
• Must say - Gin Liqueur
Nice to have
• Some sort of floral or swirley background detail would be nice
Should not have
• Must not appeal to children

```html
<!DOCTYPE html>
<html lang="en">
<head>
<meta charset="utf-8">
<title>Shimmering Pink Strawberry Gin Liqueur – 500ml Label</title>
<link rel="stylesheet" href="https://fonts.googleapis.com/css2?family=Cinzel:wght@900&family=Oswald:wght@500;600;700&display=swap">
<style>
  :root {
    --ink: #0b0b0b;
    --paper: #ffffff;
    --blush: #f59296;
    --blush-light: #fbd4d5;
    --blush-mid: #f2aeb0;
    --berry: #b3121c;
    --berry-dark: #5e0a10;
    --stage-light: #cfcfcf;
    --stage-dark: #4a4a4a;
  }
  * { box-sizing: border-box; margin: 0; padding: 0; }
  html, body {
    width: 1200px;
    height: 1000px;
    overflow: hidden;
  }
  body {
    background: linear-gradient(135deg, var(--stage-light) 0%, #8f8f8f 55%, var(--stage-dark) 100%);
    font-family: "Oswald", "Arial Narrow", sans-serif;
    position: relative;
  }
  .label {
    position: absolute;
    left: 190px;
    top: 90px;
    width: 568px;
    height: 568px;
    transform: scale(1.4437);
    transform-origin: 0 0;
    background: var(--paper);
    overflow: hidden;
  }
  .label__top-bar {
    position: absolute;
    left: 0; top: 0;
    width: 100%; height: 25px;
    background: var(--ink);
  }
  .label__top-band {
    position: absolute;
    left: 0; top: 25px;
    width: 100%; height: 18px;
    background: linear-gradient(90deg, var(--blush) 0%, var(--blush-light) 100%);
  }
  .brand-tab {
    position: absolute;
    left: 27px; top: 6px;
    width: 175px; height: 168px;
  }
  .brand-tab svg { position: absolute; inset: 0; }
  .brand-tab__name {
    position: absolute;
    left: 0; width: 154px; top: 30px;
    text-align: center;
    font-weight: 600;
    font-size: 27px;
    line-height: 1.12;
    color: var(--ink);
  }
  .product-line {
    position: absolute;
    font-weight: 700;
    color: var(--ink);
    text-transform: uppercase;
    line-height: 1;
    white-space: nowrap;
  }
  .product-line--shimmering {
    right: 38px; top: 150px;
    font-size: 58px;
    letter-spacing: 1px;
  }
  .product-line--strawberry {
    left: 30px; top: 360px;
    font-size: 58px;
    letter-spacing: 1px;
  }
  .product-line--type {
    right: 30px; top: 382px;
    font-size: 27px;
    font-weight: 600;
  }
  .pink-word {
    position: absolute;
    left: 24px; top: 218px;
    width: 508px; height: 130px;
    display: flex;
    justify-content: space-between;
    align-items: center;
    font-family: "Cinzel", "Times New Roman", serif;
    font-weight: 900;
    font-size: 138px;
    line-height: 1;
    color: var(--berry);
  }
  .label__bottom-bar {
    position: absolute;
    left: 0; top: 493px;
    width: 100%; height: 44px;
    background: var(--ink);
    color: var(--paper);
    font-weight: 600;
    font-size: 24px;
    letter-spacing: 1px;
  }
  .label__volume { position: absolute; left: 65px; top: 4px; }
  .label__abv { position: absolute; right: 68px; top: 4px; }
  .label__bottom-band {
    position: absolute;
    left: 0; top: 537px;
    width: 100%; height: 31px;
    background: linear-gradient(90deg, var(--blush) 0%, var(--blush-light) 100%);
  }
</style>
</head>
<body>
  <main class="label">
    <div class="label__top-bar"></div>
    <div class="label__top-band"></div>

    <div class="brand-tab">
      <svg width="175" height="168" viewBox="0 0 175 168" aria-hidden="true">
        <defs>
          <linearGradient id="tabFill" x1="0" y1="0" x2="1" y2="1">
            <stop offset="0" stop-color="#fbd4d5"/>
            <stop offset="1" stop-color="#f2aeb0"/>
          </linearGradient>
        </defs>
        <path d="M0 14 Q0 0 14 0 L160 0 Q175 0 175 12 L175 20 L154 20 L154 168 L0 168 Z" fill="url(#tabFill)"/>
        <path d="M154 20 L175 20 Q175 8 164 8 Q154 8 154 20 Z" fill="#f59296"/>
      </svg>
      <p class="brand-tab__name">Harlow<br>Vale<br>Distillers</p>
    </div>

    <h1 class="product-line product-line--shimmering">Shimmering</h1>
    <p class="pink-word" aria-label="PINK"><span>P</span><span>I</span><span>N</span><span>K</span></p>
    <p class="product-line product-line--strawberry">Strawberry</p>
    <p class="product-line product-line--type">- Gin Liqueur</p>

    <div class="label__bottom-bar">
      <span class="label__volume">500ML</span>
      <span class="label__abv">18.75% VOL</span>
    </div>
    <div class="label__bottom-band"></div>
  </main>
</body>
</html>
```